Wealth Education Business Needs Sharp Business Card Design

We need a business card design for a recently launched investor education business called Harbor Crest.

The final design should promote security, empowerment, self improvement and financial gain. The card will ideally promote the stature of the business.

For more information and colours please visit harborcrest.com.au

Target Market(s)

Corporate executives and high net worth individuals

Industry/Entity Type

Education

Contact Information for Business Card

Name
Position
Contact Address
Phone
Mobile
Email
Website

```html
<!DOCTYPE html>
<html lang="en">
<head>
<meta charset="utf-8">
<title>Harbor Crest Business Card</title>
<link href="https://fonts.googleapis.com/css2?family=Michroma&family=Exo+2:wght@400;500&display=swap" rel="stylesheet">
<style>
  :root {
    --backdrop: #e4e4e2;
    --paper: #f7f7f7;
    --paper-shade: #e6e6e6;
    --charcoal: #403c3c;
    --teal: #12706c;
    --teal-dark: #0b4f4c;
    --ink: #3a3a3a;
    --white: #ffffff;
  }
  * { margin: 0; padding: 0; box-sizing: border-box; }
  html, body { width: 1200px; height: 869px; overflow: hidden; }
  body { background: var(--backdrop); position: relative; font-family: "Exo 2", sans-serif; }

  .card {
    position: absolute;
    width: 620px; height: 354px;
    background: linear-gradient(135deg, var(--white) 0%, var(--paper) 50%, var(--paper-shade) 100%);
    box-shadow: 0 10px 28px rgba(0,0,0,0.22);
    overflow: hidden;
  }
  .card-front { left: 80px; top: 60px; }
  .card-back { left: 500px; top: 455px; }

  .front-brand {
    position: absolute; inset: 0;
    display: flex; flex-direction: column; align-items: center; justify-content: center; gap: 22px;
  }
  .brand-dot { width: 70px; height: 70px; border-radius: 50%; background: var(--teal); }
  .brand-name {
    font-family: "Michroma", sans-serif;
    color: var(--ink);
    font-size: 38px; letter-spacing: 6px;
    white-space: nowrap;
  }

  .back-shapes { position: absolute; inset: 0; }
  .back-brand {
    position: absolute; left: 34px; top: 42px;
    display: flex; align-items: center; gap: 12px;
  }
  .back-brand .brand-dot { width: 30px; height: 30px; }
  .back-brand .brand-name { font-size: 20px; letter-spacing: 3px; }

  .address {
    position: absolute; left: 134px; top: 111px;
    color: var(--white); font-size: 13px; letter-spacing: 0.3px; white-space: nowrap;
  }
  .person { position: absolute; right: 22px; top: 112px; text-align: right; color: var(--ink); }
  .person-name { font-family: "Michroma", sans-serif; font-size: 16px; letter-spacing: 0.5px; white-space: nowrap; }
  .person-role { font-family: "Michroma", sans-serif; font-size: 8.5px; letter-spacing: 1px; margin-top: 4px; white-space: nowrap; }

  .contact-list { position: absolute; list-style: none; color: var(--white); font-size: 15px; letter-spacing: 0.5px; }
  .contact-web { left: 30px; top: 166px; }
  .contact-phone { left: 410px; top: 232px; }
  .contact-list li { display: flex; align-items: center; gap: 12px; height: 34px; white-space: nowrap; }
  .icon {
    width: 24px; height: 24px; background: var(--white); border-radius: 3px;
    display: flex; align-items: center; justify-content: center;
  }
</style>
</head>
<body>
  <section class="card card-front">
    <div class="front-brand">
      <span class="brand-dot"></span>
      <span class="brand-name">HARBOR CREST</span>
    </div>
  </section>

  <section class="card card-back">
    <svg class="back-shapes" width="620" height="354" viewBox="0 0 620 354">
      <polygon points="0,140 400,140 432,190 620,190 620,354 0,354" fill="var(--charcoal)"/>
      <polygon points="100,100 120,100 120,120" fill="var(--teal-dark)"/>
      <polygon points="120,100 390,100 425,140 120,140" fill="var(--teal)"/>
      <polygon points="390,100 425,140 405,140" fill="var(--teal-dark)"/>
      <rect x="0" y="306" width="620" height="28" fill="var(--teal)"/>
    </svg>

    <div class="back-brand">
      <span class="brand-dot"></span>
      <span class="brand-name">HARBOR CREST</span>
    </div>

    <p class="address">214, 9th floor, Quayside Tower Marsh Lane</p>

    <div class="person">
      <p class="person-name">DANIEL HART</p>
      <p class="person-role">GENERAL MANAGER</p>
    </div>

    <ul class="contact-list contact-web">
      <li>
        <span class="icon">
          <svg width="16" height="16" viewBox="0 0 16 16" fill="none" stroke="var(--charcoal)" stroke-width="1.4">
            <circle cx="8" cy="8" r="6.5"/><ellipse cx="8" cy="8" rx="3" ry="6.5"/><line x1="1.5" y1="8" x2="14.5" y2="8"/>
          </svg>
        </span>
        www.harborcrest.com.au
      </li>
      <li>
        <span class="icon">
          <svg width="16" height="16" viewBox="0 0 16 16" fill="none" stroke="var(--charcoal)" stroke-width="1.4">
            <rect x="1.5" y="3.5" width="13" height="9"/><polyline points="1.5,3.5 8,9 14.5,3.5"/>
          </svg>
        </span>
        daniel@harborcrest.com.au
      </li>
    </ul>

    <ul class="contact-list contact-phone">
      <li>
        <span class="icon">
          <svg width="16" height="16" viewBox="0 0 16 16">
            <path d="M4 2 L6.5 2 L7 5 L5.5 6 Q6.5 9 9.5 10.5 L10.5 9 L14 9.5 L14 12 Q13 14 11 14 Q3 12 2 4 Q2 2 4 2 Z" fill="var(--charcoal)"/>
          </svg>
        </span>
        012 555 0148
      </li>
      <li>
        <span class="icon">
          <svg width="16" height="16" viewBox="0 0 16 16">
            <rect x="4" y="1" width="8" height="14" rx="1.5" fill="var(--charcoal)"/>
            <rect x="5.3" y="3" width="5.4" height="8" fill="var(--white)"/>
            <circle cx="8" cy="13" r="0.9" fill="var(--white)"/>
          </svg>
        </span>
        012 555 0148
      </li>
    </ul>
  </section>
</body>
</html>
```